Website Design for NYC Female Attorney – Clean, Warm, Professional

Maren Holbeck, Esq.
www.MarenTHolbeckLegal.example

I’m a New York City-based attorney and CPA with a reputation for providing thoughtful, high-integrity legal guidance in both estate planning and small business law. I’ve served over 500 clients, and maintain a perfect 5-star rating. Clients come to me for clarity, compassion, and results — and I want my new website to reflect that.

**🎯 WHAT I NEED:**
A clean, modern, and emotionally resonant website that highlights who I am, what I do, and why clients trust me. It must feel approachable and warm, but still professional and elegant — think Quorvex meets boutique law firm. Feminine but not frilly.

**🧩 CORE WEBSITE SECTIONS (Top Navigation):**

1. **Home** – Strong first impression, tagline, CTA (book a call)
Homepage Copy (Sample Layout)
Headline:
Trusted Legal Guidance for Families and Founders.

Subheading:
Whether you’re protecting what you’ve built or building what’s next, I help you navigate estate planning and business law with confidence, compassion, and clarity.

Tagline (beneath logo or footer):
Legal Clarity for Life and Business.
2. **About Maren** – Bio, personal approach, credentials
3. **Services**

* *Estate Planning*
* *Business Law*
4. **Who I Work With** – Ideal clients (parents, entrepreneurs, etc.)
5. **Testimonials** – Client praise and social proof
6. **Success Stories** – Highlighting wins and case types
7. **FAQs** – Warm and clear answers to common questions
8. **Blog** – Thought leadership and helpful tips
8.5 Events
9. **Contact / Book a Call** – Scheduling or contact form

**🖼 STYLE DIRECTION:**

* Clean white backgrounds, soft jewel tones or neutrals
* Professional headshots and personal branding assets available
* Emphasis on readability, trust, and ease of navigation - THIS NEEDS TO BE BUILT OUT SO IT IS TRUSTED BY AI!
* No harsh colors, no corporate/legal clichés (e.g., gavels or scales) - I MEAN THIS. I DO NOT WANT A BORING LAW WEBSITE WITH SCALES AND GAVELS
* Feminine edge (not pink-heavy), with strong hierarchy and callouts

**💡 DESIGN NOTES:**

* Mobile-first design required
* Should include space for video or welcome message
* Easy to update blog or CMS area preferred
* Built in a user-friendly platform like WordPress, Webflow, or similar
* Needs to feel elevated enough to support high-end flat fee packages

**📣 TONE:**
Smart. Warm. Sophisticated. Human.

**⚖️ FINAL DELIVERABLES:**

* Homepage + 5+ interior pages
* Desktop + mobile views
* Style guide (fonts, colors, buttons)
* Bonus if you can help with copy layout/structure (not just visuals)

**📍TARGET AUDIENCE:**

* Busy professionals and families in NYC
* Women and couples who want peace of mind
* Entrepreneurs and creatives needing solid legal support

Here is my current site: www.MarenTHolbeckLegal.example
And here is a second business I have: www.QuickDayCounselDesk.example

Target Market(s)

Families and business owners

Industry/Entity Type

Law

Number of Pages Required

5+ page

Font styles to use
Serif
Sans Serif
Script

Requirements
Must have
• This website must be built to be seen as trustworthy by AI.

```html
<!DOCTYPE html>
<html lang="en">
<head>
<meta charset="utf-8">
<title>Maren Holbeck, Esq. — Estate Planning &amp; Business Law</title>
<link href="https://fonts.googleapis.com/css2?family=Poppins:wght@400;500;600;700&family=Playfair+Display:wght@500;600&family=Dancing+Script:wght@600&display=swap" rel="stylesheet">
<style>
:root{
  --navy:#2b2f86;
  --navy-deep:#23266f;
  --ink:#1f2140;
  --muted:#5d5f78;
  --pink:#e0559b;
  --pink-soft:#f9dceb;
  --pink-pale:#fdf0f6;
  --lav:#efecf8;
  --line:#e4e0ef;
  --white:#ffffff;
  --gold:#f5b82e;
}
*{box-sizing:border-box;margin:0;padding:0}
html,body{width:1200px;height:5300px;overflow:hidden}
body{font-family:"Poppins",Arial,sans-serif;color:var(--ink);background:var(--white);font-size:14px;line-height:1.55}
section,header,footer{position:relative;width:1200px}
.label{font-size:12px;color:var(--navy);font-weight:500;display:flex;align-items:center;gap:8px}
.label::before{content:"";width:18px;height:2px;background:var(--pink)}
.btn{display:inline-flex;align-items:center;gap:8px;background:var(--navy);color:#fff;border-radius:24px;padding:11px 22px;font-size:13px;font-weight:500;white-space:nowrap}
.btn::after{content:"›";font-size:16px;line-height:1}
.stars{color:var(--gold);letter-spacing:2px;font-size:15px}

/* nav */
.site-nav{height:80px;display:flex;align-items:center;justify-content:space-between;padding:0 60px;background:var(--white)}
.brand{font-family:"Playfair Display",Georgia,serif;font-size:16px;letter-spacing:3px;color:var(--navy);display:flex;align-items:center;gap:8px}
.brand i{width:10px;height:10px;border-radius:50%;background:var(--pink);display:block}
.nav-links{display:flex;gap:30px;font-size:13px;color:var(--ink);align-items:center}

/* hero */
.hero{height:690px;background:linear-gradient(100deg,#fff 0%,var(--pink-pale) 45%,var(--pink-soft) 100%);padding:70px 60px 0}
.hero h1{font-size:40px;line-height:1.15;font-weight:700;color:var(--navy);width:580px}
.hero-lead{width:480px;margin-top:16px;color:var(--muted);font-size:15px}
.hero .btn{margin-top:24px}
.review-brands{display:flex;gap:18px;margin-top:22px;font-weight:600;font-size:14px;color:var(--ink)}
.rating{display:flex;align-items:center;gap:10px;margin-top:14px;font-weight:600}
.clients{display:flex;align-items:center;gap:10px;margin-top:10px;font-size:12px;color:var(--muted)}
.avatars{display:flex}
.avatars span{width:26px;height:26px;border-radius:50%;border:2px solid #fff;margin-left:-8px;background:#d9b7c9}
.avatars span:first-child{margin-left:0;background:#c4a1b7}
.stats{display:flex;gap:16px;margin-top:26px}
.stat{width:120px;height:96px;background:#fff;border-radius:12px;box-shadow:0 6px 18px rgba(43,47,134,.08);padding:14px 16px}
.stat b{display:block;font-size:28px;color:var(--pink);font-weight:600;line-height:1.1}
.stat small{font-size:11px;color:var(--muted)}
.hero-photo{position:absolute;left:660px;top:32px;width:440px;height:590px;border-radius:22px;background:linear-gradient(160deg,#e8c9c2,#d8a3ad 55%,#c98aa0)}

/* about */
.about{height:260px;padding:50px 60px 0}
.about h2{font-size:24px;color:var(--navy);margin-top:10px;font-weight:600}
.about .role{font-size:13px;color:var(--muted);margin-top:8px}
.about-text{position:absolute;left:520px;top:80px;width:600px;font-size:14px;color:var(--muted)}

/* services */
.services{height:500px}
.services-box{position:absolute;left:180px;top:0;width:840px;height:460px;background:var(--pink-soft);border-radius:14px;padding:36px 60px;text-align:center}
.services-box .label{justify-content:center}
.services-box h2{font-size:26px;color:var(--navy);font-weight:600;margin-top:8px}
.services-box p{font-size:12px;color:var(--muted)}
.service-grid{display:grid;grid-template-columns:1fr 1fr;gap:12px 24px;margin-top:28px;text-align:left}
.service-grid li{list-style:none;background:#fff;border-radius:6px;padding:11px 16px;font-size:13px;color:var(--navy);display:flex;justify-content:space-between}
.service-grid li::after{content:"›";color:var(--pink)}

/* blog */
.blog{height:700px;background:linear-gradient(180deg,var(--pink-pale),var(--pink-soft));padding:70px 60px 0;text-align:center}
.blog .label{justify-content:center}
.blog h2{font-size:28px;color:var(--navy);font-weight:600;line-height:1.25;margin-top:8px}
.blog .sub{font-size:12px;color:var(--muted)}
.blog-cards{display:flex;gap:24px;margin-top:34px;text-align:left}
.blog-card{flex:1;height:380px;background:#fff;border-radius:12px;padding:28px;position:relative}
.blog-card h3{font-size:19px;line-height:1.3;color:var(--navy);font-weight:600}
.blog-card p{font-size:13px;color:var(--muted);margin-top:18px}
.blog-card .btn{position:absolute;left:28px;bottom:28px}

/* overview */
.overview{height:400px;padding:70px 60px 0}
.overview h2{font-size:28px;color:var(--navy);font-weight:600;line-height:1.25;width:420px;margin-top:8px}
.overview p{width:420px;font-size:13px;color:var(--muted);position:absolute;top:250px}
.video-frame{position:absolute;left:560px;top:40px;width:540px;height:320px;border:4px solid #f4a9cd;border-radius:12px;overflow:hidden;background:#fff}
.video-frame .media{position:absolute;inset:0 0 46px 0;background:linear-gradient(135deg,#eef4f8,#d9e7ef 60%,#c9dbe6)}
.video-frame .caption{position:absolute;left:0;right:0;bottom:0;height:46px;background:var(--navy);color:#fff;font-size:11px;padding:8px 16px;line-height:1.4}

/* faq */
.faq{height:660px;background:var(--lav);padding:60px 120px 0}
.faq h2{font-size:26px;color:var(--navy);font-weight:600;text-align:center;margin-bottom:28px}
.faq-item{display:flex;align-items:center;justify-content:space-between;height:62px;border-bottom:1px solid var(--line);font-size:15px;color:var(--navy)}
.faq-item span{display:flex;gap:14px;align-items:center}
.faq-item span::before{content:"";width:8px;height:8px;border-radius:50%;background:var(--pink)}
.faq-item b{font-weight:400;font-size:22px}

/* testimonials */
.testimonials{height:480px;background:var(--lav);padding:20px 60px 0}
.testimonials .label{justify-content:center}
.testimonials h2{font-size:18px;color:var(--navy);text-align:center;font-weight:600;margin-top:6px}
.t-cards{display:flex;gap:20px;margin-top:22px}
.t-card{flex:1;height:260px;background:var(--navy);color:#fff;border-radius:10px;padding:18px;position:relative}
.t-card.light{background:#fff;color:var(--ink);border:2px solid #f4a9cd}
.t-head{display:flex;gap:10px;align-items:center}
.t-head i{width:36px;height:36px;border-radius:50%;background:#c9b3cf;display:block}
.t-head b{font-size:14px;display:block;line-height:1.2}
.t-head small{font-size:10px;opacity:.75}
.t-card p{font-size:11.5px;margin-top:14px;line-height:1.55}
.t-foot{position:absolute;left:18px;right:18px;bottom:14px;display:flex;justify-content:space-between;font-weight:600}
.t-bottom{display:flex;justify-content:space-between;align-items:center;margin-top:24px}
.t-bottom h3{font-size:22px;color:var(--navy);font-weight:600}
.arrows{display:flex;gap:10px}
.arrows span{width:34px;height:34px;border-radius:50%;background:#fff;color:var(--navy);display:flex;align-items:center;justify-content:center}
.arrows span.on{background:var(--pink);color:#fff}

/* events */
.events{height:520px;padding:40px 60px 0}
.events h2{position:absolute;left:520px;top:36px;font-size:24px;color:var(--navy);font-weight:600;width:620px}
.events .sub{position:absolute;left:520px;top:74px;width:600px;font-size:12px;color:var(--muted)}
.event-art{position:absolute;left:60px;top:120px;width:420px;height:340px;border-radius:10px;background:linear-gradient(135deg,#fff 0%,#fbe0ee 55%,#f2a5ca 100%);border:1px solid var(--line)}
.event-list{position:absolute;left:520px;top:130px;width:620px}
.event{display:flex;justify-content:space-between;align-items:flex-start;padding:14px 0;border-bottom:1px solid var(--line);height:108px}
.event h3{font-size:17px;color:var(--navy);font-weight:600;width:440px;line-height:1.3}
.event p{font-size:11px;color:var(--muted);margin-top:6px;width:440px}
.event .btn{padding:8px 16px;font-size:11px}

/* contact */
.contact{height:440px;background:linear-gradient(180deg,#fff,var(--pink-pale))}
.script{position:absolute;font-family:"Dancing Script",cursive;color:var(--pink);font-size:44px;white-space:nowrap}
.contact-card{position:absolute;left:400px;top:90px;width:400px;height:320px;background:#fff;border-radius:14px;box-shadow:0 8px 26px rgba(43,47,134,.1);padding:26px 40px;text-align:center}
.contact-card h2{font-size:20px;color:var(--navy);font-weight:600}
.contact-card p{font-size:11px;color:var(--muted)}
.field{height:34px;border-bottom:1px solid var(--line);text-align:left;font-size:11px;color:#9a9bb0;padding-top:14px}
.contact-card .btn{margin-top:18px;padding:9px 20px;font-size:12px}

/* footer */
.site-footer{height:500px;background:linear-gradient(180deg,var(--pink-soft),#f6c7dc);padding:40px 60px 0}
.footer-logo{width:240px;height:150px;background:#fff;border-radius:6px;display:flex;align-items:center;justify-content:center}
.tagline{position:absolute;left:420px;top:80px;font-family:"Playfair Display",Georgia,serif;font-size:40px;color:var(--navy);font-weight:500}
.footer-cols{position:absolute;left:60px;top:250px;right:60px;display:flex;justify-content:space-between;font-size:13px;color:var(--navy)}
.footer-links{width:240px;display:flex;flex-wrap:wrap;gap:8px 16px}
.footer-bottom{position:absolute;left:60px;right:60px;bottom:24px;display:flex;justify-content:space-between;font-size:11px;color:var(--muted);border-top:1px solid rgba(43,47,134,.15);padding-top:12px}
</style>
</head>
<body>

<header class="site-nav">
  <div class="brand"><i></i>MAREN HOLBECK</div>
  <nav class="nav-links">
    <span>About</span><span>Services</span><span>Blog</span><span>Events</span><span>Clients</span>
    <span class="btn">Book a Call</span>
  </nav>
</header>

<section class="hero">
  <h1>Trusted Legal Guidance for Families and Founders.</h1>
  <p class="hero-lead">Whether you’re protecting what you’ve built or building what’s next, I help you navigate estate planning and business law with confidence, compassion, and clarity.</p>
  <span class="btn">Get Started Today</span>
  <div class="review-brands"><span>Searchly</span><span>Counselrank</span><span>Reviewhub</span></div>
  <div class="rating"><span class="stars">★★★★★</span> 5.0</div>
  <div class="clients"><div class="avatars"><span></span><span></span><span></span></div>From 500+ clients</div>
  <div class="stats">
    <div class="stat"><b>500+</b><small>Clients helped</small></div>
    <div class="stat"><b>$2M+</b><small>Secured in fees</small></div>
    <div class="stat"><b>#2</b><small>Ranked in NY</small></div>
  </div>
  <div class="hero-photo" role="img" aria-label="Portrait photograph of the attorney in a light blouse"></div>
</section>

<section class="about">
  <div class="label">About Maren</div>
  <h2>Maren T. Holbeck, Esq., CPA</h2>
  <div class="role">Founder and Managing Attorney</div>
  <p class="about-text">Meet Maren Holbeck, an award-winning estate planning attorney ranked as the 2nd best in New York. Maren knows how to build a thriving practice. She’s here to teach you how to take your estate planning practice to the next level with her QuickDay Counsel Desk program.</p>
</section>

<section class="services">
  <div class="services-box">
    <div class="label">Services</div>
    <h2>Comprehensive Estate Planning &amp; Business Law</h2>
    <p>Schedule Your Peace of Mind Planning Session</p>
    <ul class="service-grid">
      <li>Comprehensive Estate Plans</li><li>Special Needs Trusts</li>
      <li>Revocable Living Trusts</li><li>Irrevocable Special-Use Trusts</li>
      <li>Powers of Attorney</li><li>Business Succession Planning</li>
      <li>Advanced Health Care Directives</li><li>Asset Protection Entities</li>
      <li>Last Wills and Testaments</li><li>Non-Citizen Estate Planning</li>
    </ul>
  </div>
</section>

<section class="blog">
  <div class="label">Blog</div>
  <h2>Your Comprehensive Guide to<br>Inheritance Planning and Business Law</h2>
  <p class="sub">Explore easy-to-understand articles designed to empower you to make informed legal decisions.</p>
  <div class="blog-cards">
    <article class="blog-card">
      <h3>Get Your Peace of Mind: What to Expect from Your Free Planning Session</h3>
      <p>Learn 5 simple steps in our 60-minute Meetwell session that will answer your questions, map out your options and give you clarity on your financial and family future.</p>
      <span class="btn">Schedule Your Session Now</span>
    </article>
    <article class="blog-card">
      <h3>Why Inheritance Planning is Not Just for the Rich: Protect Your Family Today</h3>
      <p>Understand how wills, trusts and powers of attorney protect your loved ones and your assets, regardless of the size of your wealth.</p>
      <span class="btn">Schedule Your Session Now</span>
    </article>
    <article class="blog-card">
      <h3>Business Succession: Ensure Your Business Legacy is Secure and Sustainable</h3>
      <p>Explore how proper succession planning can keep your business going and protect the value you’ve built.</p>
      <span class="btn">Schedule Your Session Now</span>
    </article>
  </div>
</section>

<section class="overview">
  <div class="label">Overview of the process</div>
  <h2>See How We Help You Plan for the Future</h2>
  <p>Watch our introduction video to get to know our approach to helping you achieve your estate and business planning goals.</p>
  <div class="video-frame">
    <div class="media" role="img" aria-label="Welcome video still with an illustrated attorney beside a planning document"></div>
    <div class="caption">Business ownership includes what your business or owner/partnership is held, especially as it passes to loved ones.</div>
  </div>
</section>

<section class="faq">
  <h2>Get Answers to Your Questions on Inheritance Planning and Business Law.</h2>
  <div class="faq-item"><span>How can I learn more about Maren Holbeck?</span><b>+</b></div>
  <div class="faq-item"><span>How can I learn more about the Law Office of Maren T. Holbeck?</span><b>+</b></div>
  <div class="faq-item"><span>What is our general process?</span><b>+</b></div>
  <div class="faq-item"><span>What can I expect from my Peace of Mind Planning Session?</span><b>+</b></div>
  <div class="faq-item"><span>What are the initial steps to get started?</span><b>+</b></div>
  <div class="faq-item"><span>What kind of information do you need from me?</span><b>+</b></div>
  <div class="faq-item"><span>What is estate planning?</span><b>+</b></div>
</section>

<section class="testimonials">
  <div class="label">Testimonials</div>
  <h2>See What Happens When People Choose Us to Grow!</h2>
  <div class="t-cards">
    <article class="t-card light">
      <div class="t-head"><i></i><div><b>Delia Marston</b><small>Comprehensive Estate Plan</small></div></div>
      <p>Maren was incredibly organized and efficient. She provided clear instructions and advice, which were easy to follow, resulting in a straightforward and stress-free experience. I recommend Maren for her exceptional advice.</p>
      <div class="t-foot"><span class="stars">★★★★★</span><span>5.0</span></div>
    </article>
    <article class="t-card">
      <div class="t-head"><i></i><div><b>Corin Vale</b><small>Powers of Attorney</small></div></div>
      <p>Highly recommend hiring Maren as a trust and estates attorney. She was exceptionally patient, understanding, skilled and knowledgeable. Maren took the time to carefully explain my options and ensure I felt comfortable throughout.</p>
      <div class="t-foot"><span class="stars">★★★★★</span><span>5.0</span></div>
    </article>
    <article class="t-card">
      <div class="t-head"><i></i><div><b>Osric Penhale</b><small>Client</small></div></div>
      <p>Maren was very responsive and great at simplifying everything so I could understand. Very efficient on her end, and I would use her again.</p>
      <div class="t-foot"><span class="stars">★★★★★</span><span>5.0</span></div>
    </article>
    <article class="t-card">
      <div class="t-head"><i></i><div><b>Tamsin Ferrow</b><small>Client</small></div></div>
      <p>Maren is THE expert in this practice, she is kind, patient, knowledgeable, professional, and has a wonderful sense of humor. I could not be in better hands for guidance and recommend her to anyone looking for a true professional.</p>
      <div class="t-foot"><span class="stars">★★★★★</span><span>5.0</span></div>
    </article>
  </div>
  <div class="t-bottom">
    <h3>Trusted by 500+ clients and counting.</h3>
    <div class="arrows"><span>‹</span><span class="on">›</span></div>
  </div>
</section>

<section class="events">
  <div class="label">Events</div>
  <h2>Grow your Practice &amp; Business: Our Exclusive Event</h2>
  <p class="sub">Join webinars and interactive sessions with experts to gain the latest insights and strategies to elevate your practice.</p>
  <div class="event-art" role="img" aria-label="Event promo graphic for Pricing Like a Pro with speaker portrait"></div>
  <div class="event-list">
    <div class="event"><div><h3>Pricing Like a Pro: How to Stop Charging Like You’re in Survival Mode</h3><p>Most lawyers undercharge and work too hard. Learn simple pricing that supports a calm, profitable practice. 15 May, 2025</p></div><span class="btn">Register Now</span></div>
    <div class="event"><div><h3>The New KPIs for Small Firms: It’s Not Just About Revenue Anymore</h3><p>12 May, 2025</p></div><span class="btn">Register Now</span></div>
    <div class="event"><div><h3>The Case for Slow Growth: Why Scaling Too Fast Will Wreck Your Life</h3><p>12 May, 2025</p></div><span class="btn">Register Now</span></div>
  </div>
</section>

<section class="contact">
  <span class="script" style="left:120px;top:150px;transform:rotate(-28deg)">Any Questions?</span>
  <span class="script" style="left:470px;top:10px">Any Questions?</span>
  <span class="script" style="left:860px;top:140px;transform:rotate(28deg)">Any Questions?</span>
  <div class="contact-card">
    <h2>Any Questions?</h2>
    <p>We’d look forward to answering your questions.</p>
    <div class="field">Name</div>
    <div class="field">Email</div>
    <div class="field">Phone</div>
    <div class="field">Message</div>
    <span class="btn">Discuss the problem</span>
  </div>
</section>

<footer class="site-footer">
  <div class="footer-logo"><div class="brand"><i></i>MAREN HOLBECK</div></div>
  <div class="tagline">Legal Clarity for Life and Business.</div>
  <div class="footer-cols">
    <div class="footer-links"><span>About</span><span>Service</span><span>Clients</span><span>Contact</span><span>FAQs</span><span>Testimonials</span><span>Blog</span><span>Events</span><span>Success Stories</span></div>
    <div>48 Larkspur Ave, Fl 9<br>New York, NY 10099</div>
    <div>48 Larkspur Ave, Fl 9<br>New York, NY 10099</div>
    <div>hello@marenholbeck.example</div>
  </div>
  <div class="footer-bottom"><span>© Copyright Law Office of Maren Holbeck 2025</span><span>Privacy Policy</span><span>Terms &amp; Conditions</span></div>
</footer>

</body>
</html>
```